New Business Card Design Project

I farm pacific oysters, once they are harvested they sell to seafood markets and processors. The main selling point of the product I have is that the oysters are grown on a very isolated stretch of coastline of the far west coast of south australia that has the purest sea water quality. It is also a very Eco friendly and self sustainable industry. The sea state in this particular area is quite rugged and that helps to sculpture the shells into a uniform and displayable half shell.

Industry/Entity Type

Farm

Requirements
Must have
• name: Gregory Tandell
phone no: 0487312645
e-mail: tandell_greg@quillpost.example
address: P.O box 7
gullet cove 5692 south Australia
Should not have
• do not include title/job description

```html
<!DOCTYPE html>
<html lang="en">
<head>
<meta charset="utf-8">
<title>Tidemark Oysters – Business Card</title>
<link rel="stylesheet" href="https://fonts.googleapis.com/css2?family=Open+Sans:wght@400;600;700&display=swap">
<style>
  :root {
    --page-bg: #e9ecef;
    --card-bg: #ffffff;
    --teal-dark: #0f4f6e;
    --teal-mid: #1a7898;
    --teal-light: #2a9bb8;
    --grey-band: #8a8d91;
    --grey-light: #c3c6c9;
    --ink-white: #ffffff;
  }
  html, body {
    margin: 0;
    padding: 0;
    width: 1200px;
    height: 976px;
    overflow: hidden;
    background: var(--page-bg);
    font-family: "Open Sans", Arial, sans-serif;
  }
  .sheet {
    position: relative;
    width: 1200px;
    height: 976px;
  }
  .card {
    position: absolute;
    left: 240px;
    width: 720px;
    height: 412px;
    background: var(--card-bg);
    border-radius: 22px;
    overflow: hidden;
    box-shadow: 0 6px 18px rgba(0,0,0,0.12);
  }
  .card--back { top: 50px; }
  .card--front { top: 514px; }
  .card svg { display: block; }

  .brand {
    position: absolute;
    display: flex;
    align-items: center;
    gap: 16px;
  }
  .brand__mark {
    width: 74px;
    height: 74px;
    border-radius: 50%;
    background: var(--teal-mid);
    flex: none;
  }
  .brand__name {
    font-weight: 700;
    color: var(--teal-dark);
    font-size: 34px;
    line-height: 1.05;
  }
  .card--back .brand { left: 0; right: 0; top: 158px; justify-content: center; }

  .card--front .brand { left: 408px; top: 104px; }
  .card--front .brand__mark { width: 64px; height: 64px; }
  .card--front .brand__name { font-size: 30px; }

  .holder-name {
    position: absolute;
    left: 458px;
    top: 214px;
    margin: 0;
    font-size: 21px;
    line-height: 1.2;
    font-weight: 700;
    color: var(--teal-mid);
    white-space: nowrap;
  }

  .contact {
    position: absolute;
    left: 34px;
    top: 128px;
    margin: 0;
    padding: 0;
    list-style: none;
    color: var(--ink-white);
    font-size: 14px;
    line-height: 1.35;
  }
  .contact__item {
    display: flex;
    align-items: flex-start;
    gap: 9px;
    margin-bottom: 9px;
  }
  .contact__icon {
    flex: none;
    width: 16px;
    height: 16px;
    margin-top: 1px;
  }
</style>
</head>
<body>
<main class="sheet">

  <section class="card card--back" aria-label="Business card back">
    <div class="brand">
      <span class="brand__mark" aria-hidden="true"></span>
      <span class="brand__name">Tidemark Oysters</span>
    </div>
  </section>

  <section class="card card--front" aria-label="Business card front">
    <svg class="card__waves" width="720" height="412" viewBox="0 0 720 412" aria-hidden="true">
      <defs>
        <linearGradient id="tealPanel" x1="0" y1="0" x2="1" y2="1">
          <stop offset="0" stop-color="var(--teal-dark)"/>
          <stop offset="0.55" stop-color="var(--teal-light)"/>
          <stop offset="1" stop-color="var(--teal-dark)"/>
        </linearGradient>
      </defs>
      <path class="wave-grey-light" d="M225,0 C330,70 300,300 720,346 L720,370 C300,330 300,80 195,0 Z" fill="var(--grey-light)"/>
      <path class="wave-grey" d="M200,0 C320,80 290,310 720,360 L720,378 C290,336 290,90 178,0 Z" fill="var(--grey-band)"/>
      <path class="wave-teal" d="M0,0 L170,0 C290,90 260,330 720,392 L720,412 L0,412 Z" fill="url(#tealPanel)"/>
    </svg>

    <ul class="contact">
      <li class="contact__item">
        <svg class="contact__icon" viewBox="0 0 16 16" aria-hidden="true">
          <circle cx="8" cy="8" r="8" fill="var(--ink-white)"/>
          <path d="M8 3.5a3 3 0 0 0-3 3c0 2.2 3 5.6 3 5.6s3-3.4 3-5.6a3 3 0 0 0-3-3zm0 4.1a1.1 1.1 0 1 1 0-2.2 1.1 1.1 0 0 1 0 2.2z" fill="var(--teal-mid)"/>
        </svg>
        <span>P.O box 7<br>Gullet Cove 5692 South Australia</span>
      </li>
      <li class="contact__item">
        <svg class="contact__icon" viewBox="0 0 16 16" aria-hidden="true">
          <circle cx="8" cy="8" r="8" fill="var(--ink-white)"/>
          <path d="M5.4 4.2l1.4-.3.8 2-1 .8a5.5 5.5 0 0 0 2.7 2.7l.8-1 2 .8-.3 1.4c-3.6.4-6.8-2.8-6.4-6.4z" fill="var(--teal-mid)"/>
        </svg>
        <span>0487312645</span>
      </li>
      <li class="contact__item">
        <svg class="contact__icon" viewBox="0 0 16 16" aria-hidden="true">
          <circle cx="8" cy="8" r="8" fill="var(--ink-white)"/>
          <rect x="4" y="5" width="8" height="6" rx="0.8" fill="var(--teal-mid)"/>
          <path d="M4.3 5.4L8 8.3l3.7-2.9" fill="none" stroke="var(--ink-white)" stroke-width="0.9"/>
        </svg>
        <span>tandell_greg@quillpost.example</span>
      </li>
    </ul>

    <div class="brand">
      <span class="brand__mark" aria-hidden="true"></span>
      <span class="brand__name">Tidemark<br>Oysters</span>
    </div>

    <p class="holder-name">Gregory Tandell</p>
  </section>

</main>
</body>
</html>
```